Roof Plumbing Company needs simple, modern business card using the attached logo and below details:

Glen Marwick
Kestrel Roofing Pty Ltd
ABN: 58 217 934 062
Phone: 0417 286 503
Email: kestrelroofing@mailvista.com
Website: kestrelroofing.com.au

For all of your metal roof plumbing requirements contact Kestrel Roofing for an obligation free quote - no job too big or to small!

Industry/Entity Type

Business

Contact Information for Business Card

Glen Marwick
Kestrel Roofing Pty Ltd
ABN 58 217 934 062
0417 286 503
kestrelroofing@mailvista.com
kestrelroofing.com.au

Requirements
Must have
• Bright eye catching design, professional look

```html
<!DOCTYPE html>
<html lang="en">
<head>
<meta charset="utf-8">
<title>Kestrel Roofing Business Card</title>
<link rel="stylesheet" href="https://fonts.googleapis.com/css2?family=Nunito+Sans:wght@400;600;800&display=swap">
<style>
  :root {
    --red: #d42027;
    --red-dark: #a8161c;
    --red-mid: #c81e24;
    --ink: #2b2b2b;
    --paper: #ffffff;
    --backdrop: #ecebe8;
  }
  * { margin: 0; padding: 0; box-sizing: border-box; }
  html, body { width: 1200px; height: 1000px; overflow: hidden; }
  body {
    background: var(--backdrop);
    font-family: "Nunito Sans", Arial, sans-serif;
    position: relative;
  }
  .card {
    position: absolute;
    left: 265px;
    width: 666px;
    height: 397px;
    box-shadow: 0 6px 14px rgba(0,0,0,0.25);
    overflow: hidden;
  }
  .card--front { top: 73px; background: var(--paper); }
  .card--back {
    top: 532px;
    background: linear-gradient(160deg, var(--red) 0%, var(--red-mid) 55%, var(--red-dark) 100%);
  }

  .brand {
    position: absolute;
    left: 34px;
    top: 150px;
    width: 300px;
    color: var(--red);
    font-weight: 800;
    text-align: center;
    line-height: 1;
  }
  .brand__name { font-size: 58px; letter-spacing: 1px; }
  .brand__entity { font-size: 19px; letter-spacing: 3px; margin-top: 10px; }

  .contact {
    position: absolute;
    left: 383px;
    top: 88px;
    color: var(--ink);
  }
  .contact__name {
    color: var(--red);
    font-weight: 800;
    font-size: 24px;
    letter-spacing: 0.5px;
    margin-bottom: 34px;
  }
  .contact__abn { font-size: 17px; margin-bottom: 8px; }
  .contact__row {
    display: flex;
    align-items: center;
    gap: 8px;
    font-size: 17px;
    height: 26px;
  }
  .contact__row svg { width: 16px; height: 16px; flex: none; }

  .tagline {
    position: absolute;
    left: 0;
    top: 310px;
    width: 100%;
    height: 66px;
    background: linear-gradient(180deg, var(--red) 0%, var(--red-dark) 100%);
    color: var(--paper);
    font-size: 16px;
    line-height: 22px;
    text-align: center;
    padding-top: 11px;
  }

  .back-brand {
    position: absolute;
    left: 340px;
    top: 215px;
    width: 300px;
    color: var(--paper);
    font-weight: 800;
    text-align: center;
    line-height: 1;
  }
  .back-brand__name { font-size: 58px; letter-spacing: 1px; }
  .back-brand__entity { font-size: 19px; letter-spacing: 3px; margin-top: 14px; }
  .rule {
    position: absolute;
    top: 356px;
    height: 2px;
    background: var(--paper);
  }
  .rule--left { left: 0; width: 330px; }
  .rule--right { left: 626px; width: 40px; }
</style>
</head>
<body>
  <section class="card card--front">
    <div class="brand">
      <div class="brand__name">KESTREL</div>
      <div class="brand__entity">ROOFING PTY LTD</div>
    </div>

    <div class="contact">
      <div class="contact__name">GLEN MARWICK</div>
      <div class="contact__abn">ABN 58 217 934 062</div>
      <div class="contact__row">
        <svg viewBox="0 0 16 16" aria-hidden="true"><path fill="#d42027" d="M3.6 1.5l2.2 2.6-1.2 1.6c.8 2 2.3 3.5 4.3 4.4l1.6-1.2 2.6 2.2-1.4 2.4C6.4 13.3 2.7 9.6 1.2 4.3z"/></svg>
        <span>0417 286 503</span>
      </div>
      <div class="contact__row">
        <svg viewBox="0 0 16 16" aria-hidden="true"><rect x="1" y="3.5" width="14" height="9.5" fill="#d42027"/><path d="M1.5 4l6.5 5 6.5-5" stroke="#fff" stroke-width="1.2" fill="none"/></svg>
        <span>kestrelroofing@mailvista.com</span>
      </div>
      <div class="contact__row">
        <svg viewBox="0 0 16 16" aria-hidden="true"><circle cx="8" cy="8" r="6.5" fill="none" stroke="#d42027" stroke-width="1.6"/><path d="M1.5 8h13M8 1.5c-2.5 3-2.5 10 0 13M8 1.5c2.5 3 2.5 10 0 13" stroke="#d42027" stroke-width="1.2" fill="none"/></svg>
        <span>kestrelroofing.com.au</span>
      </div>
    </div>

    <div class="tagline">For all of your metal roof plumbing requirements contact Kestrel Roofing for<br>an obligation free quote - no job too big or to small!</div>
  </section>

  <section class="card card--back">
    <div class="back-brand">
      <div class="back-brand__name">KESTREL</div>
      <div class="back-brand__entity">ROOFING PTY LTD</div>
    </div>
    <div class="rule rule--left"></div>
    <div class="rule rule--right"></div>
  </section>
</body>
</html>
```